Brochure design for healthcare software company

We need a tri-fold brochure design for our healthcare software company that provides software and services for clinicians who manage patients who have or may be diagnosed with cancer.

We have an existing web, business card design and trade show booth design and want the ultimate design to be consistent with these. All of the files including stock images are provided.

Target Market(s)

Nurses, Healthcare professionals

Industry/Entity Type

Healthcare

Requirements
Must have
• Design consistent with attached tradeshow booth and business card.

```html
<!DOCTYPE html>
<html lang="en">
<head>
<meta charset="utf-8">
<title>Veltrana Navigation – Tri-fold Brochure Inside</title>
<link href="https://fonts.googleapis.com/css2?family=Open+Sans:wght@400;600&display=swap" rel="stylesheet">
<style>
  :root {
    --page-bg: #d9d9d9;
    --paper: #f7f7f7;
    --brand-blue: #1d5fb1;
    --brand-blue-deep: #0c3c8a;
    --heading-blue: #1d5aa8;
    --brand-green: #1f9a4a;
    --body-text: #3a3a3a;
    --white: #ffffff;
  }
  * { box-sizing: border-box; margin: 0; padding: 0; }
  html, body { width: 1200px; height: 870px; overflow: hidden; }
  body {
    background: var(--page-bg);
    font-family: "Open Sans", Arial, sans-serif;
    color: var(--body-text);
  }
  .brochure {
    position: absolute; left: 30px; top: 30px;
    width: 1140px; height: 810px;
    display: flex;
    box-shadow: 0 8px 24px rgba(0,0,0,.18);
  }
  .panel { position: relative; width: 380px; height: 810px; overflow: hidden; background: var(--paper); }
  .panel svg.art { position: absolute; left: 0; top: 0; }
  .copy { position: absolute; left: 34px; right: 34px; }
  .section-title {
    font-weight: 400; font-size: 17px; letter-spacing: .3px;
    text-transform: uppercase; text-align: center; margin-bottom: 12px;
    color: var(--heading-blue);
  }
  .section-text { font-size: 14.5px; line-height: 1.45; text-align: justify; margin-bottom: 16px; }
  .section-title--spaced { margin-top: 26px; }

  .panel--blue { background: linear-gradient(160deg, var(--brand-blue) 0%, var(--brand-blue-deep) 100%); color: var(--white); }
  .panel--blue .section-title,
  .panel--blue .section-text { color: var(--white); }
  .paper-stack {
    position: absolute; left: 110px; top: 440px; width: 160px; height: 160px;
    border-radius: 50%; border: 6px solid #cfd6e2;
    background: radial-gradient(circle at 50% 55%, #f2ede0 0%, #d9d3c4 50%, #6c6c6c 100%);
  }
</style>
</head>
<body>
<main class="brochure">

  <section class="panel panel--left">
    <svg class="art" width="380" height="810" viewBox="0 0 380 810">
      <rect role="img" aria-label="Photo of a smiling clinician taking notes in a hospital corridor" x="0" y="0" width="380" height="300" fill="#a9b7c6"/>
      <path d="M0 300 C 110 215, 260 205, 380 230 L380 810 L0 810 Z" fill="var(--brand-green)"/>
      <path d="M0 345 C 110 255, 260 240, 380 265 L380 810 L0 810 Z" fill="var(--paper)"/>
    </svg>
    <div class="copy" style="top:320px">
      <h2 class="section-title">Simplified Navigation</h2>
      <p class="section-text">Track all of your patients from their entry point, for example an abnormal screening exam or a positive diagnosis, through survivorship.</p>
      <p class="section-text">Veltrana Navigation allows you to easily maintain a record of all referrals, exams, treatments, contacts, appointments and notes for your patients.</p>
      <h2 class="section-title section-title--spaced">Advanced Workflow Tools</h2>
      <p class="section-text">View and manage your entire patient load in a single dynamic work list area.</p>
      <p class="section-text">Completely customizable to match your workflow. Create checklists for every step of your workflow to maintain consistent patient care and monitoring.</p>
    </div>
  </section>

  <section class="panel panel--blue">
    <div class="copy" style="top:44px">
      <h2 class="section-title">Reporting and Analytics</h2>
      <p class="section-text">Quickly demonstrate the value of your navigation efforts with deep analytics and reporting. View current and historical trends for any or all of your facilities and staff, including detailed reporting on work loads, time to care, patient barriers, referrals and appointments.</p>
    </div>
    <div class="copy" style="top:262px">
      <h2 class="section-title">Eliminate Paper</h2>
      <p class="section-text">Manage all of your paperwork and patient forms in one easy to use area. Automatically create document packets and auto fill forms for patients or referrals with a single click.</p>
    </div>
    <div class="paper-stack" role="img" aria-label="Photo of a stack of paper files"></div>
    <div class="copy" style="top:640px">
      <h2 class="section-title">Integrated</h2>
      <p class="section-text">Reduce double data entry by integrating the systems you already have. Patients can be seamlessly added and updated without manual efforts.</p>
    </div>
  </section>

  <section class="panel panel--right">
    <svg class="art" width="380" height="810" viewBox="0 0 380 810">
      <rect role="img" aria-label="Illustration of a tablet showing blue charts and graphs" x="60" y="40" width="260" height="170" rx="10" fill="#c9dbef"/>
      <path d="M0 520 C 120 430, 270 420, 380 440 L380 810 L0 810 Z" fill="var(--brand-green)"/>
      <path role="img" aria-label="Photo of a smiling nurse on the phone holding a patient file" d="M0 550 C 120 465, 270 455, 380 475 L380 810 L0 810 Z" fill="#c8b9a2"/>
    </svg>
    <div class="copy" style="top:250px">
      <h2 class="section-title">Secure</h2>
      <p class="section-text">Built from the ground up with security in mind, Veltrana Navigation is completely HIPAA compliant.</p>
      <p class="section-text">Rest assured that your, and your patients data is protected.</p>
    </div>
  </section>

</main>
</body>
</html>
```